Home page concept, possible logo colour change

There is no need to code a home page, we are just looking for concept ideas.
We have had a logo designed for a new company we are starting named Corvenhall Aluminium Windows & Doors. We are manufacturing bullet resistant window frames. We have had logo designed, we like the concept of the design, but the current colours (black and red) may not be the best option, especially when designing the website home page, and how it interacts with the logo colours. I have also attached the first draft of the home page which we are not happy with. The overall design/navigation is good, we have issues with the darkened out primary image and also the amount of red on the page, it just doesn't feel right. As mentioned before we are happy to look at colour changes to the logo.
Number of Pages Required
1 page
Look and feel
Each slider illustrates characteristics of the customer's brand and the style your logo design should communicate.

```html
<!DOCTYPE html>
<html lang="en">
<head>
<meta charset="utf-8">
<title>Corvenhall Aluminium Windows &amp; Doors</title>
<link href="https://fonts.googleapis.com/css2?family=Mulish:wght@400;600;700;800&family=Rajdhani:wght@600;700&display=swap" rel="stylesheet">
<style>
:root{
  --green:#07933f;
  --green-soft:#dceee3;
  --ink:#1d1d1d;
  --text:#3b3b3b;
  --muted:#5a5a5a;
  --paper:#f4f3f3;
  --footer:#1b1b1b;
  --white:#ffffff;
}
*{margin:0;padding:0;box-sizing:border-box}
html,body{width:1200px;height:3986px;overflow:hidden}
body{font-family:"Mulish",sans-serif;color:var(--text);background:var(--white);position:relative}
.abs{position:absolute}
h1,h2,h3,h4{font-family:"Rajdhani",sans-serif;color:var(--ink);font-weight:700;letter-spacing:.5px}
.btn{display:inline-block;background:var(--green);color:var(--white);font-weight:800;border-radius:5px;text-decoration:none;text-align:center}
p{line-height:1.45}

/* header */
.site-header{top:0;left:0;width:1200px;height:96px;background:var(--white)}
.brand{left:131px;top:24px}
.brand-name{font-size:27px;font-weight:800;color:var(--ink);display:flex;align-items:center;gap:8px}
.brand-name i{width:12px;height:12px;border-radius:50%;background:var(--green);display:inline-block}
.brand-sub{font-size:7.5px;font-weight:700;letter-spacing:1px;text-transform:uppercase;color:var(--ink);margin-top:2px}
.nav{top:36px;left:566px;display:flex;gap:34px;font-size:16px;color:var(--text)}
.nav a{color:inherit;text-decoration:none;padding-bottom:4px}
.nav a.active{color:var(--green);border-bottom:2px solid var(--green)}
.nav-cta{left:916px;top:27px;width:152px;height:37px;line-height:37px;font-size:16px;font-weight:600}

/* hero */
.hero{top:96px;left:0;width:1200px;height:594px;background:linear-gradient(180deg,#9fbfdc 0%,#c7d4de 22%,#d3c8b8 40%,#e9e6e0 60%,#c9b9a2 100%)}
.hero-title{top:170px;width:1200px;text-align:center;color:var(--white);font-size:60px;line-height:64px;text-shadow:0 2px 6px rgba(0,0,0,.35)}
.hero-lead{top:312px;width:1200px;text-align:center;color:var(--white);font-size:20px;font-weight:800;line-height:29px;text-shadow:0 2px 5px rgba(0,0,0,.35)}
.hero-btn{left:545px;top:398px;width:110px;height:42px;line-height:42px;font-size:13px}
.dots{top:548px;left:567px;display:flex;gap:10px}
.dots span{width:14px;height:14px;border-radius:50%;border:2px solid var(--white)}
.dots span.on{background:var(--green)}

/* why */
.why{top:690px;left:0;width:1200px;height:504px;background:linear-gradient(160deg,#e4e4e4,#f1f1f1 50%,#e2e2e2)}
.why-photo{left:132px;top:55px;width:335px;height:390px;background:linear-gradient(180deg,#d6dde3,#e4ded3 55%,#b9a38d)}
.why-text{left:546px;top:58px;width:500px}
.why-text h2{font-size:25px}
.why-text>p{font-size:13px;margin-top:10px}
.feature{display:flex;gap:25px;margin-top:30px}
.feature-ico{flex:none;width:64px;height:64px;border-radius:50%;background:var(--green);display:flex;align-items:center;justify-content:center}
.feature h3{font-size:20px}
.feature p{font-size:12.5px;margin-top:6px}

/* benefits */
.benefits{top:1194px;left:0;width:1200px;height:615px;background:var(--white)}
.benefits h2{position:absolute;left:131px;top:40px;font-size:26px}
.benefits .intro{position:absolute;left:131px;top:94px;font-size:14px;width:900px}
.benefit{position:absolute;width:265px}
.benefit svg{display:block;height:50px}
.benefit h3{font-size:19px;margin-top:22px}
.benefit p{font-size:12.5px;margin-top:10px}
.vline{position:absolute;width:3px;height:155px;background:var(--green)}

/* products */
.products{top:1809px;left:0;width:1200px;height:541px;background:var(--paper)}
.center-head{position:absolute;width:1200px;text-align:center}
.center-head h2{font-size:27px}
.center-head p{font-size:16px;margin-top:6px}
.product-photo{position:absolute;background:linear-gradient(135deg,#3a3d40,#8f979e 50%,#2a2c2e)}
.product{position:absolute;width:180px}
.product h3{font-size:20px}
.product p{font-size:12.5px;margin-top:10px}
.product .btn{margin-top:18px;width:84px;height:32px;line-height:32px;font-size:10.5px}
.prod-divider{left:622px;top:164px;width:2px;height:304px;background:var(--green)}
.prod-cap{left:584px;width:76px;height:2px;background:var(--green)}

/* features */
.features{top:2350px;left:0;width:1200px;height:708px;background:linear-gradient(180deg,#f6f6f6,#ededed)}
.blob{position:absolute;border-radius:50%;background:var(--green-soft)}
.plus{position:absolute;width:46px;height:46px;border-radius:50%;background:var(--green);display:flex;align-items:center;justify-content:center}
.callout{position:absolute;width:280px}
.callout h4{font-size:16px}
.callout p{font-size:12.5px;margin-top:8px}

/* safe home */
.safe{top:3058px;left:0;width:516px;height:560px;background:var(--green);color:var(--white)}
.safe h2{position:absolute;left:131px;top:42px;color:var(--white);font-size:28px}
.safe .tag{position:absolute;left:131px;top:80px;font-size:16px}
.safe .copy{position:absolute;left:131px;top:114px;width:290px;font-size:12.5px}
.field{position:absolute;left:136px;width:315px;background:var(--white);color:var(--muted);font-size:12px;padding:11px 15px}
.submit{position:absolute;left:136px;top:474px;width:315px;height:36px;background:var(--white);color:var(--green);font-family:"Rajdhani",sans-serif;font-weight:700;font-size:17px;text-align:center;line-height:36px;letter-spacing:1px}
.family-photo{top:3058px;left:516px;width:684px;height:560px;background:linear-gradient(135deg,#eef0ee,#d8d4cc 45%,#c09d7e 75%,#8e7a66)}

/* footer */
.footer{top:3618px;left:0;width:1200px;height:368px;background:var(--footer);color:#e6e6e6}
.f-brand{left:131px;top:98px}
.f-brand .brand-name{font-size:42px;color:var(--white)}
.f-brand .brand-sub{font-size:11px;color:var(--white);letter-spacing:2px;margin-top:4px}
.f-col{position:absolute;top:42px}
.f-col h4{color:var(--white);font-size:15px;padding-bottom:8px;border-bottom:2px solid #d9d9d9}
.f-item{display:flex;gap:14px;align-items:flex-start;font-size:11.5px;line-height:1.4;margin-top:16px;white-space:nowrap}
.f-dot{flex:none;width:23px;height:23px;border-radius:50%;background:var(--green);display:flex;align-items:center;justify-content:center}
.f-menu a{display:block;color:#e6e6e6;text-decoration:none;font-size:11.5px;line-height:19px}
.f-rule{left:131px;top:282px;width:934px;height:2px;background:#d9d9d9}
.copyright{top:320px;width:1200px;text-align:center;font-size:11px}
</style>
</head>
<body>

<header class="abs site-header">
  <div class="abs brand">
    <div class="brand-name">Corvenhall <i></i></div>
    <div class="brand-sub">Aluminium Windows &amp; Doors</div>
  </div>
  <nav class="abs nav">
    <a class="active" href="#">Home</a>
    <a href="#">Products</a>
    <a href="#">Why Corvenhall</a>
  </nav>
  <a class="abs btn nav-cta" href="#">Make an Enquiry</a>
</header>

<section class="abs hero" role="img" aria-label="Photo of a modern house exterior with white garage door, stone cladding and wall lantern">
  <h1 class="abs hero-title">BULLET RESISTANT<br>WINDOW &amp; DOORS</h1>
  <p class="abs hero-lead">Lorem ipsum dolor sit amet consectetur adipi<br>scing elit sed do eiusmod tempor</p>
  <a class="abs btn hero-btn" href="#">READ MORE</a>
  <div class="abs dots"><span class="on"></span><span></span><span></span></div>
</section>

<section class="abs why">
  <div class="abs why-photo" role="img" aria-label="Photo of white arched windows on a rendered house inside a decorative shield frame"></div>
  <div class="abs why-text">
    <h2>WHY CORVENHALL</h2>
    <p>Lorem ipsum dolor sit amet, consectetur adipiscing elit, sed do eiusmod tempor incididunt ut labore et dolore magna aliqua.</p>
    <div class="feature">
      <div class="feature-ico"><svg width="34" height="34" viewBox="0 0 24 24" fill="none" stroke="#fff" stroke-width="1.8"><path d="M12 2l8 3v6c0 5-3.5 9-8 11-4.5-2-8-6-8-11V5z"/><path d="M8.5 12l2.5 2.5 4.5-5"/></svg></div>
      <div><h3>Premium Protection</h3><p>Lorem ipsum dolor sit amet, consectetur adipiscing elit, sed do eiusmod tempor incididunt ut labore et dolore magna aliqua.</p></div>
    </div>
    <div class="feature">
      <div class="feature-ico"><svg width="32" height="32" viewBox="0 0 24 24" fill="none" stroke="#fff" stroke-width="1.8"><rect x="5" y="3" width="12" height="18"/><path d="M9 3v18M13 12h2M19 8v4M17 10h4"/></svg></div>
      <div><h3>Aesthetically Designed</h3><p>Lorem ipsum dolor sit amet, consectetur adipiscing elit, sed do eiusmod tempor incididunt ut labore et dolore magna aliqua.</p></div>
    </div>
    <div class="feature">
      <div class="feature-ico"><svg width="36" height="36" viewBox="0 0 24 24" fill="none" stroke="#fff" stroke-width="1.8"><path d="M3 7h11v9H3zM14 10h4l3 3v3h-7"/><circle cx="7" cy="17.5" r="1.8"/><circle cx="17" cy="17.5" r="1.8"/></svg></div>
      <div><h3>Promptly Delivered</h3><p>Lorem ipsum dolor sit amet, consectetur adipiscing elit, sed do eiusmod tempor incididunt ut labore et dolore magna aliqua.</p></div>
    </div>
  </div>
</section>

<section class="abs benefits">
  <h2>PRODUCT BENEFITS</h2>
  <p class="intro">Lorem ipsum dolor sit amet, consectetur adipiscing elit, sed do eiusmod tempor incididunt ut labore et dolore magna aliqua.<br>Ut enim ad minim veniam, quis nostrud exercitation ullamco</p>

  <div class="benefit" style="left:131px;top:176px">
    <svg width="50" viewBox="0 0 24 24" fill="none" stroke="#07933f" stroke-width="1.8"><path d="M3 9h4l5-4v14l-5-4H3z" fill="#07933f"/><path d="M15 9a4 4 0 010 6M18 6a8 8 0 010 12M3 3l18 18"/></svg>
    <h3>ACOUSTICAL</h3><p>Lorem ipsum dolor sit amet consectetur adipiscing elit sed do eiusmod tempor incididunt ut labore et dolore.</p>
  </div>
  <div class="vline" style="left:422px;top:178px"></div>
  <div class="benefit" style="left:470px;top:176px">
    <svg width="50" viewBox="0 0 24 24" fill="none" stroke="#07933f" stroke-width="1.8"><path d="M12 2l8 3v6c0 5-3.5 9-8 11-4.5-2-8-6-8-11V5z"/><rect x="9" y="11" width="6" height="5" fill="#07933f"/><path d="M10 11V9a2 2 0 014 0v2"/></svg>
    <h3>GSA VAULT DOORS</h3><p>Lorem ipsum dolor sit amet consectetur adipiscing elit sed do eiusmod tempor incididunt ut labore et dolore.</p>
  </div>
  <div class="vline" style="left:764px;top:178px"></div>
  <div class="benefit" style="left:816px;top:176px">
    <svg width="50" viewBox="0 0 24 24" fill="none" stroke="#07933f" stroke-width="1.8"><path d="M20 3c-5 0-9 3-11 8l4 4c5-2 8-6 7-12z" fill="#07933f"/><path d="M7 13l-3 3M9 16l-4 4M11 18l-3 3"/></svg>
    <h3>BULLET RESISTANT</h3><p>Lorem ipsum dolor sit amet consectetur adipiscing elit sed do eiusmod tempor incididunt ut labore et dolore.</p>
  </div>

  <div class="benefit" style="left:131px;top:391px">
    <svg width="50" viewBox="0 0 24 24" fill="none" stroke="#07933f" stroke-width="1.8"><circle cx="12" cy="12" r="10"/><path d="M12 4v2M5 12h2M17 12h2M7 7l1.4 1.4M17 7l-1.4 1.4M12 16l1-7"/><path d="M8 19h8"/></svg>
    <h3>PRESSURE RESISTANT</h3><p>Lorem ipsum dolor sit amet consectetur adipiscing elit sed do eiusmod tempor incididunt ut labore et dolore.</p>
  </div>
  <div class="vline" style="left:422px;top:393px"></div>
  <div class="benefit" style="left:470px;top:391px">
    <svg width="50" viewBox="0 0 24 24" fill="#07933f"><circle cx="12" cy="12" r="2.2"/><path d="M10 9L7 3.5A10 10 0 0117 3.5L14 9a3.5 3.5 0 00-4 0zM8.6 13.6L2.3 14a10 10 0 005 8.6l3-5.3a3.5 3.5 0 01-1.7-3.7zM15.4 13.6l6.3.4a10 10 0 01-5 8.6l-3-5.3a3.5 3.5 0 001.7-3.7z"/></svg>
    <h3>RADIATION SHIELDING</h3><p>Lorem ipsum dolor sit amet consectetur adipiscing elit sed do eiusmod tempor incididunt ut labore et dolore.</p>
  </div>
  <div class="vline" style="left:764px;top:393px"></div>
  <div class="benefit" style="left:816px;top:391px">
    <svg width="54" viewBox="0 0 24 24" fill="none" stroke="#07933f" stroke-width="1.4"><circle cx="9" cy="9" r="3"/><path d="M9 2v2M9 14v2M2 9h2M14 9h2M4 4l1.4 1.4M12.6 12.6L14 14M4 14l1.4-1.4M12.6 5.4L14 4"/><circle cx="16.5" cy="16.5" r="2.3"/><path d="M16.5 11.5v2M16.5 19.5v2M11.5 16.5h2M19.5 16.5h2"/></svg>
    <h3>HARDWARE</h3><p>Lorem ipsum dolor sit amet consectetur adipiscing elit sed do eiusmod tempor incididunt ut labore et dolore.</p>
  </div>
</section>

<section class="abs products">
  <div class="center-head" style="top:44px"><h2>OUR PRODUCTS</h2><p>Lorem ipsum dolor sit amet, consectetur adipiscing elit sed do eiusmod</p></div>
  <div class="product-photo" style="left:136px;top:178px;width:218px;height:300px" role="img" aria-label="Product photo of a black aluminium window frame"></div>
  <div class="product" style="left:411px;top:218px">
    <h3>WINDOW</h3>
    <p>Lorem ipsum dolor sit amet consectetur adipiscing elit sed do eiusmod tempor incididunt ut labore et dolore. quis nostrud exercitation ullamco laboris nisi ut aliquip</p>
    <a class="btn" href="#">READ MORE</a>
  </div>
  <div class="abs prod-cap" style="top:164px"></div>
  <div class="abs prod-divider"></div>
  <div class="abs prod-cap" style="top:467px"></div>
  <div class="product" style="left:663px;top:218px">
    <h3>DOOR</h3>
    <p>Lorem ipsum dolor sit amet consectetur adipiscing elit sed do eiusmod tempor incididunt ut labore et dolore. quis nostrud exercitation ullamco laboris nisi ut aliquip</p>
    <a class="btn" href="#">READ MORE</a>
  </div>
  <div class="product-photo" style="left:910px;top:166px;width:158px;height:316px" role="img" aria-label="Product photo of a black aluminium glazed door, slightly open"></div>
</section>

<section class="abs features">
  <div class="center-head" style="top:40px"><h2>FEATURES</h2><p>Lorem ipsum dolor sit amet, consectetur adipiscing elit sed do eiusmod</p></div>
  <div class="blob" style="left:386px;top:154px;width:170px;height:170px"></div>
  <div class="blob" style="left:650px;top:380px;width:150px;height:150px"></div>
  <div class="product-photo" style="left:432px;top:160px;width:335px;height:395px" role="img" aria-label="Product photo of a black aluminium window frame, angled"></div>
  <div class="plus" style="left:738px;top:135px"><svg width="22" height="22" viewBox="0 0 22 22" stroke="#fff" stroke-width="2.5"><path d="M11 2v18M2 11h18"/></svg></div>
  <div class="plus" style="left:429px;top:332px"><svg width="22" height="22" viewBox="0 0 22 22" stroke="#fff" stroke-width="2.5"><path d="M11 2v18M2 11h18"/></svg></div>
  <div class="plus" style="left:626px;top:533px"><svg width="22" height="22" viewBox="0 0 22 22" stroke="#fff" stroke-width="2.5"><path d="M11 2v18M2 11h18"/></svg></div>
  <div class="callout" style="left:815px;top:135px"><h4>EXPLORE OUR RANGE</h4><p>Lorem ipsum dolor sit amet consectetur adipiscing elit sed do eiusmod tempor incididunt ut labore et dolore. quis nos trud exercitation ullamco laboris nisi ut aliquip</p></div>
  <div class="callout" style="left:159px;top:316px;width:240px"><h4>MAKE AN ENQUIRY</h4><p>Lorem ipsum dolor sit amet consectetur adipiscing elit sed do eiusmod tempor incididunt ut labore et dolore. quis nos trud exercitation ullamco laboris nisi ut aliquip</p></div>
  <div class="callout" style="left:688px;top:576px;width:290px"><h4>CUSTOMISED QUOTES</h4><p>Lorem ipsum dolor sit amet consectetur adipiscing elit sed do eiusmod tempor incididunt ut labore et dolore. quis nos trud exercitation ullamco laboris nisi ut aliquip</p></div>
</section>

<section class="abs safe">
  <h2>SAFE HOME</h2>
  <p class="tag">Protect who you love</p>
  <p class="copy">Lorem ipsum dolor sit amet consectetur adipiscing elit sed do eiusmod tempor incididunt ut labore et dolore. quis nos trud exercitation ullamco laboris nisi ut aliquip</p>
  <div class="field" style="top:202px;height:36px">Name</div>
  <div class="field" style="top:248px;height:36px">Email</div>
  <div class="field" style="top:294px;height:36px">Phone</div>
  <div class="field" style="top:340px;height:122px">Message</div>
  <div class="submit">SUBMIT</div>
</section>
<div class="abs family-photo" role="img" aria-label="Photo of a family playing on the floor at home with their pet dog"></div>

<footer class="abs footer">
  <div class="abs brand f-brand">
    <div class="brand-name">Corvenhall <i></i></div>
    <div class="brand-sub">Aluminium Windows &amp; Doors</div>
  </div>
  <div class="f-col" style="left:501px;width:192px">
    <h4>CONTACT US</h4>
    <div class="f-item"><span class="f-dot"><svg width="11" height="11" viewBox="0 0 24 24" fill="#fff"><path d="M12 2a7 7 0 00-7 7c0 5 7 13 7 13s7-8 7-13a7 7 0 00-7-7zm0 9.5a2.5 2.5 0 110-5 2.5 2.5 0 010 5z"/></svg></span><span>48 Harrowmere Rd, Eastvale,<br>ON K0X 2B4, Canada</span></div>
    <div class="f-item"><span class="f-dot"><svg width="11" height="11" viewBox="0 0 24 24" fill="#fff"><path d="M6.6 10.8a15 15 0 006.6 6.6l2.2-2.2a1 1 0 011-.25 11 11 0 003.6.6 1 1 0 011 1V20a1 1 0 01-1 1A17 17 0 013 4a1 1 0 011-1h3.5a1 1 0 011 1c0 1.25.2 2.45.6 3.6a1 1 0 01-.25 1z"/></svg></span><span>Call Us<br>+1 555 014 2280</span></div>
    <div class="f-item"><span class="f-dot"><svg width="11" height="11" viewBox="0 0 24 24" fill="#fff"><path d="M3 5h18v14H3zm2 2v.5l7 5 7-5V7l-7 5z"/></svg></span><span>E mail Us<br>info@corvenhall.com</span></div>
  </div>
  <div class="f-col f-menu" style="left:777px;width:108px">
    <h4>MENU</h4>
    <div style="margin-top:12px"><a href="#">Home</a><a href="#">Products</a><a href="#">Why Corvenhall</a><a href="#">Make an Enquiry</a></div>
  </div>
  <div class="f-col" style="left:961px;width:104px">
    <h4>FOLLOW US</h4>
    <div class="f-item" style="margin-top:22px"><span class="f-dot"></span><span>Like us on<br>FRIENDLINK</span></div>
    <div class="f-item"><span class="f-dot"></span><span>Follow us on<br>CHIRPER</span></div>
    <div class="f-item"><span class="f-dot"></span><span>Follow us on<br>WORKWIRE</span></div>
  </div>
  <div class="abs f-rule"></div>
  <p class="abs copyright">Copyright © 2023 All Rights Reserved</p>
</footer>

</body>
</html>
```